ALL TEXT GRAPHICS TM May 2025 for Instagram

We are looking for a series of social media graphics for Instagram (new size: 4:5 (1080 x 1350 pixels) ratio that are ALL TEXT. We want the following quotes below on each graphic; one quote per graphic. AND, In very small letters at the bottom of each graphic, add @TovaMarshOnline
The look and feel of these graphics should be complimentary to the color palette attached below; but keep them simple. But the design is up to you; at the end of this document, I provided various samples of all text graphics that I like as examples.
Target Market(s)
women looking to lose weight
Look and feel

```html
<!DOCTYPE html>
<html lang="en">
<head>
<meta charset="utf-8">
<title>All Text Graphics – TM</title>
<link rel="stylesheet" href="https://fonts.googleapis.com/css2?family=Noto+Sans:wght@700&family=Tinos&display=swap">
<style>
  :root {
    --page-bg: #fbf0f1;
    --blush: #ffcce5;
    --blush-accent: #ff88c0;
    --hot-pink: #ff3399;
    --hot-pink-accent: #ff9ccc;
    --berry: #c8006e;
    --ink: #000000;
    --white: #ffffff;
    --swirl-light: #f5b4d3;
    --swirl-hot: #ff6fb7;
  }
  * { margin: 0; padding: 0; box-sizing: border-box; }
  html, body {
    width: 1200px; height: 735px; overflow: hidden;
    background: var(--page-bg);
  }
  .canvas { position: relative; width: 1200px; height: 735px; }
  .post {
    position: absolute; top: 59px; width: 494px; height: 617px;
    overflow: hidden;
    box-shadow: 0 0 4px rgba(0,0,0,0.35);
  }
  .post--soft { left: 89px; background: var(--blush); }
  .post--bold { left: 618px; background: var(--hot-pink); }
  .post__shapes { position: absolute; inset: 0; width: 494px; height: 617px; }
  .headline, .serif-line, .handle, .tagline {
    position: absolute; white-space: nowrap;
  }
  .headline {
    font-family: "Noto Sans", sans-serif; font-weight: 700;
    font-size: 36px; line-height: 41px; color: var(--ink);
    letter-spacing: -0.3px;
  }
  .serif-line {
    font-family: "Tinos", serif; font-weight: 400;
  }
  .post--soft .intro { left: 43px; top: 126px; }
  .post--soft .serif-line {
    left: 43px; top: 266px; font-size: 55px; line-height: 58px; color: var(--berry);
  }
  .post--soft .tagline { left: 0; width: 494px; text-align: center; top: 428px; padding-right: 20px; }
  .post--bold .serif-line {
    left: 41px; top: 133px; font-size: 53px; line-height: 53px; color: var(--white);
  }
  .post--bold .tagline { left: 41px; top: 380px; }
  .handle {
    right: 51px; top: 550px;
    font-family: "Noto Sans", sans-serif; font-weight: 700; font-size: 16px;
  }
  .post--soft .handle { color: var(--ink); }
  .post--bold .handle { color: var(--white); }
</style>
</head>
<body>
<main class="canvas">
  <section class="post post--soft">
    <svg class="post__shapes" viewBox="0 0 494 617" aria-hidden="true">
      <polygon points="355,0 494,0 494,158 321,95" fill="var(--blush-accent)"/>
      <polygon points="0,500 191,569 174,617 0,617" fill="var(--blush-accent)"/>
      <path d="M0 43 C 120 15, 270 40, 285 230 C 290 300, 255 400, 300 447 C 330 480, 380 490, 420 515 C 465 545, 490 575, 494 580" fill="none" stroke="var(--swirl-light)" stroke-width="1"/>
    </svg>
    <h2 class="headline intro">THIS 90-DAY PLAN<br>HELPED WOMEN<br>OVER 40 SLIM DOWN,</h2>
    <p class="serif-line">Get a tiny waist<br>and feel sexy again.</p>
    <p class="headline tagline">YOU’RE NEXT.</p>
    <p class="handle">@TovaMarshOnline</p>
  </section>

  <section class="post post--bold">
    <svg class="post__shapes" viewBox="0 0 494 617" aria-hidden="true">
      <polygon points="355,0 494,0 494,158 321,95" fill="var(--hot-pink-accent)"/>
      <polygon points="0,500 191,569 174,617 0,617" fill="var(--hot-pink-accent)"/>
      <path d="M0 43 C 120 15, 270 40, 285 230 C 290 300, 255 400, 300 447 C 330 480, 380 490, 420 515 C 465 545, 490 575, 494 580" fill="none" stroke="var(--swirl-hot)" stroke-width="1"/>
    </svg>
    <p class="serif-line">You’re doing<br>all the “right” things,<br>but your belly<br>won’t go down?</p>
    <h2 class="headline tagline">HERE’S WHAT<br>YOU HAVEN’T TRIED.</h2>
    <p class="handle">@TovaMarshOnline</p>
  </section>
</main>
</body>
</html>
```